We have an approved label for 20L kegs that match with the company name. Now we need to make another label (5 x 3.5 in) more attractive to be used in bottles. We are going to bottling (750ML) wine from kegs. We want to keep, if possible, a relation between both labels, such as the color, appeal to the concept of freshness, directly from the vineyard to your glass, eco-friendly, elegant/ artistic, new way of drinking, the solution or path to the future. We drafted a label with our vision so you can be inspired and complete our idea. Brand is Vuelo Claro (clear flight), varietal and vintage as well as volume are changeable. Company logo is also included for your reference and we would like to be included in the back label or part of it, and also the phrase Rook Wine is another element that we used for our marketing. Any further information contact us.

```html
<!DOCTYPE html>
<html lang="en">
<head>
<meta charset="utf-8">
<title>Vuelo Claro – 2017 Chardonnay bottle label</title>
<link rel="stylesheet" href="https://fonts.googleapis.com/css2?family=Amatic+SC:wght@400;700&family=Oswald:wght@400&family=Cookie&display=swap">
<style>
  :root {
    --backdrop-top: #d9dade;
    --backdrop-bottom: #eeeff1;
    --label-paper: #f1f1ef;
    --ink: #1c1c1c;
    --band: #141414;
    --band-text: #f1f1ef;
    --art-light: #b9b9b9;
    --art-dark: #8a8a8a;
  }
  * { box-sizing: border-box; margin: 0; padding: 0; }
  html, body {
    width: 1200px;
    height: 780px;
    overflow: hidden;
  }
  body {
    background: linear-gradient(180deg, var(--backdrop-top), var(--backdrop-bottom));
    display: flex;
    align-items: center;
    justify-content: center;
  }
  .bottle-label {
    position: relative;
    width: 720px;
    height: 504px;
    background: var(--label-paper);
    box-shadow: 0 10px 30px rgba(0,0,0,0.12);
    overflow: hidden;
  }
  .front-panel {
    position: absolute;
    left: 50%;
    top: 0;
    width: 300px;
    height: 460px;
    transform: translateX(-50%);
  }
  .vintage-line {
    position: absolute;
    top: 54px;
    left: 0;
    right: 0;
    display: flex;
    align-items: center;
    justify-content: center;
    gap: 14px;
    font-family: "Oswald", sans-serif;
    font-weight: 400;
    font-size: 17px;
    letter-spacing: 2px;
    color: var(--ink);
  }
  .vintage-line .dash {
    width: 12px;
    height: 2px;
    background: var(--ink);
  }
  .brand-name {
    position: absolute;
    top: 92px;
    left: 8px;
    font-family: "Amatic SC", sans-serif;
    font-weight: 400;
    color: var(--ink);
    line-height: 0.95;
  }
  .brand-name .word {
    display: block;
    font-size: 78px;
    letter-spacing: 10px;
  }
  .brand-name .word + .word {
    margin-top: 4px;
  }
  .rook-wine {
    position: absolute;
    top: 276px;
    left: 60px;
    font-family: "Cookie", cursive;
    font-size: 30px;
    color: var(--ink);
  }
  .pour-art {
    position: absolute;
    left: 186px;
    top: 240px;
    width: 114px;
    height: 220px;
    background: linear-gradient(180deg, var(--art-light), var(--art-dark));
  }
  .return-band {
    position: absolute;
    left: 0;
    right: 0;
    bottom: 0;
    height: 44px;
    background: var(--band);
    display: flex;
    align-items: center;
    justify-content: center;
    font-family: "Amatic SC", sans-serif;
    font-weight: 700;
    font-size: 19px;
    letter-spacing: 1.5px;
    color: var(--band-text);
    text-transform: uppercase;
  }
</style>
</head>
<body>
  <main class="bottle-label">
    <section class="front-panel">
      <p class="vintage-line"><span class="dash"></span>2017 CHARDONNAY<span class="dash"></span></p>
      <h1 class="brand-name"><span class="word">Vuelo</span><span class="word">Claro</span></h1>
      <p class="rook-wine">Rook Wine</p>
      <div class="pour-art" role="img" aria-label="Illustration area: a keg tap pouring a flowing ribbon of wine"></div>
    </section>
    <footer class="return-band">Return the bottle and get back 25¢ in next order</footer>
  </main>
</body>
</html>
```